A unique communication angle to crowdfunding

Looking for a fresh redesign of a crowd funding website that deals in real estate. I already have the content, but am looking to take the design to the next level.

Existing real estate crowd funding sites focus on the real estate. I want to explore communication angle that:
- puts the investor in the centre of the communication: "become a baron"
- highlights the international nature (international properties, international investors)

There's also quite a lot of copy on the site, as we need to explain the service in quite a bit of detail. There's room to reduce the copy and replace with graphics. Could also consider clicking to see different text (see our difference section in http://galafeatherpost.com)

The backend of the platform is already being worked on by a specialist crowd funding service provider.

In total there are 5 pages to be designed.

The homepage is really important. Right now it looks quite dated. It doesn't have a great layout. Note there is no mobile version of the website, so the pages need to be seen well on mobile devices. When looking at the brief, refer to the following links too:

current website:
http://pebblemarquis.com

some revisions made so far:
http://preview.stackorchard.com/7K3JT9

Attached are logo files and another file which contained copy for the pages. No need to rework the logo.

Please make sure to use the same copy in the brief on the webpages, to ensure the layouts work. Designers are free to propose images they feel work on the pages.

I would like to see if rather than tweaking the pages, it's possible to come up with a better design concept. If the 5 pages are accepted, there's a chance I'll request an additional 4 pages.
Updates

Please note the font used in the logo is called "harabara" in case you decide to use it in any of the titles, etc.

Please note there is one additional page for which we would like to review designs. Note the page would be a template to be used on all future real estate detail pages. Here is an example of the current design for reference:

http://pebblemarquis.com/projects/view/14

In total there are 5 page designs required, (homepage + 4)

Thank you

FYI -

Just a quick note to give information from similar UK real estate crowdfunding sites:
http://www.tenantheron.co.uk
http://quaystone.co.uk
https://www.vaultmeridian.com

Of the above, only quaystone has a nice clean looking landing page. Information is clear and well laid out.

Hi all, just uploaded a new file in the brief. Contains some comments and a website reference. I thought it may help to explain how we could convey international aspect as well as how we could convey images in a more modern way. This is an option you can consider, but its entirely up to you how how answer the brief. Thanks!

We would like to let you know that we have just shortlisted the best designs. Together with that, we have also passed some detailed feedback to all designers who weren't shortlisted. If we didn't contact you, please let us know. If you haven't submitted a design or are working on revisions, please note these will no longer be taken into account now. We hope you understand that we need to close the project today. Thank you all once again for your great work and design concepts. Here's hoping we meet again on a future design brief. Cheers, pebblemarquis team.

Target Market(s)

At the moment, only rich are able to buy real estate. With this service, anyone can become a landlord. Target buyers:

Young professionals, looking to diversify from stock market and lower risk
People nearing retirement, looking for stable rental incomes
Retirees - looking to supplement pensions with possibility of capital gains
Parents - looking for a way to save long term for their children (instead of low interest paying bank accounts)

Industry/Entity Type

Communication

Font styles to use
Sans Serif
Other font styles liked:
• harabara

Colors
add136
f5f9eb
959595
000000

Requirements
Must have
• Overall, the site must convey "whoever you are, you too can become a landlord", and that you don't need to be wealthy to invest in real estate. See

Communication should put the investor (or the baron) at the centre. The investor can be any of those described in the target market.

Show the aspirational side of property ownership.

In addition to the investor/baron character, the second main theme is international. No other real estate crowdfunding website highlights this.
Nice to have
• Banner could show different consumer types, to illustrate that the service can appeal to many different profiles. Refer to attached file "home page reference - brightasdew.com" as an example of how this could be done.

Aim to show the international side of the service. Properties around the world, investors around the world.

```html
<!DOCTYPE html>
<html lang="en">
<head>
<meta charset="utf-8">
<title>pebblemarquis — Pool with friends. Share any gains</title>
<link rel="stylesheet" href="https://fonts.googleapis.com/css2?family=Open+Sans:wght@400;600;700;800&display=swap">
<style>
:root{
  --green:#add136;
  --green-dark:#8fb11f;
  --mist:#f5f9eb;
  --grey:#959595;
  --grey-dark:#6f6f6f;
  --ink:#000000;
  --text:#333333;
  --soft:#777777;
  --line:#e2e2e2;
  --white:#ffffff;
  --night:#141414;
}
*{box-sizing:border-box;margin:0;padding:0}
html,body{width:1200px;height:3117px;overflow:hidden}
body{font-family:"Open Sans",Arial,sans-serif;color:var(--text);background:var(--white);position:relative}
a{color:inherit;text-decoration:none}

/* header */
.site-header{height:120px;display:flex;align-items:center;justify-content:space-between;padding:0 180px 0 168px;position:relative}
.brand{display:flex;align-items:center;gap:12px;font-weight:700;font-size:24px;color:var(--green-dark)}
.brand-dot{width:28px;height:28px;border-radius:50%;background:var(--green)}
.header-right{display:flex;flex-direction:column;align-items:flex-end;gap:18px;padding-top:14px}
.utility{display:flex;align-items:center;gap:10px}
.social-dot{width:18px;height:18px;border-radius:50%;background:var(--grey)}
.search{width:200px;height:26px;border:1px solid var(--line);border-radius:13px;font-size:11px;color:#aaa;padding:4px 12px}
.main-nav{display:flex;gap:26px;font-size:13px;font-weight:700;color:#444;text-transform:uppercase;align-items:center}
.main-nav .current{background:var(--green);color:var(--white);padding:4px 14px;border-radius:12px}

/* hero */
.hero{height:525px;position:relative;text-align:center;color:var(--white);
  background:linear-gradient(180deg,#2b2b33 0%,#4a4350 35%,#5b4f49 60%,#2a2a2e 100%)}
.hero-photo{position:absolute;inset:0}
.hero-content{position:relative;padding-top:165px}
.hero-kicker{font-size:21px;font-weight:700;letter-spacing:1px}
.hero-title{font-size:55px;font-weight:800;color:var(--green);margin-top:18px;letter-spacing:1px}
.btn-ghost{display:inline-block;margin-top:40px;border:2px solid var(--white);border-radius:22px;padding:9px 30px;font-size:14px;font-weight:700;background:rgba(0,0,0,.25)}
.hero-dots{position:absolute;left:0;right:0;top:470px;display:flex;justify-content:center;gap:8px}
.hero-dots span{width:10px;height:10px;border-radius:50%;background:rgba(255,255,255,.5)}
.hero-dots span.on{background:var(--white)}

/* intro */
.intro{height:345px;background:var(--mist);text-align:center;padding-top:96px}
.intro h1{font-size:33px;font-weight:800;color:var(--ink);line-height:1.2;letter-spacing:.5px}
.intro .lead{font-size:17px;color:var(--soft);width:860px;margin:26px auto 0;line-height:1.5}
.intro .sub{font-size:14px;color:#555;margin-top:22px;line-height:1.6}

/* split */
.split{height:240px;display:flex;position:relative}
.split-panel{flex:1;text-align:center;color:var(--white);padding-top:40px}
.split-panel.buy{background:var(--green)}
.split-panel.sell{background:var(--grey)}
.split-panel h2{font-size:28px;font-weight:800}
.split-panel p{font-size:13px;line-height:1.55;width:340px;margin:12px auto 0}
.btn-pill{display:inline-block;margin-top:22px;padding:11px 22px;border-radius:24px;font-size:14px;font-weight:700}
.btn-light{background:linear-gradient(#ffffff,#d8d8d8);color:#333}
.btn-lime{background:linear-gradient(#d2ef62,#9cc024);color:#333}
.split-badge{position:absolute;left:577px;top:97px;width:46px;height:46px;border-radius:50%;background:var(--white);border:4px solid var(--mist);display:flex;align-items:center;justify-content:center}

/* projects */
.projects{height:675px;text-align:center;padding-top:60px}
.section-title{font-size:33px;font-weight:800;color:var(--ink);letter-spacing:.5px}
.section-lead{font-size:17px;color:var(--soft);width:580px;margin:16px auto 0;line-height:1.45}
.cards{display:flex;justify-content:center;gap:36px;margin-top:48px}
.card{width:282px;height:420px;border:1px solid var(--line);background:var(--white);box-shadow:0 2px 6px rgba(0,0,0,.08);padding:18px 18px 0}
.card-price{font-size:20px;font-weight:800;color:var(--ink)}
.card-photo{height:126px;margin-top:14px;background:linear-gradient(180deg,#6fa6d8 0%,#4c7fb5 55%,#2f4d6e 100%)}
.card-title{font-size:15px;font-weight:600;color:var(--ink);margin-top:18px}
.card-text{font-size:11px;color:var(--soft);line-height:1.5;width:200px;margin:12px auto 0}
.progress{height:5px;background:#e6e6e6;margin:34px 8px 0}
.progress span{display:block;height:100%;background:var(--green)}
.funded{font-size:11px;color:#555;margin-top:8px}
.btn-card{display:inline-block;margin-top:26px;background:var(--green);color:var(--white);font-size:10px;font-weight:700;padding:6px 14px;border-radius:12px}

/* community */
.community{height:375px;background:var(--mist);text-align:center;padding-top:60px}
.features{display:flex;justify-content:center;gap:105px;margin-top:58px}
.feature{width:230px}
.feature-icon{width:60px;height:60px;border-radius:50%;background:#d4ea8a;margin:0 auto;display:flex;align-items:center;justify-content:center}
.feature p{font-size:13px;color:#555;line-height:1.5;margin-top:22px}

/* partners */
.partners{height:120px;display:flex;align-items:center;justify-content:center;gap:34px;border-bottom:1px solid var(--line)}
.partner{width:100px;height:30px;background:#cfcfcf;border-radius:3px}
.arrow{width:20px;height:20px}

/* footer */
.site-footer{height:270px;padding:40px 138px 0}
.footer-top{display:flex;justify-content:space-between;align-items:center}
.footer-nav{display:flex;gap:30px;font-size:13px;color:#333}
.footer-nav .current{color:var(--green-dark)}
.footer-bottom{display:flex;justify-content:space-between;margin-top:64px}
.footer-about{font-size:13px;line-height:1.6;width:680px;color:#333}
.parent-brand{text-align:right}
.parent-brand strong{display:block;font-size:30px;font-weight:700;color:#555;line-height:1}
.parent-brand small{font-size:11px;color:var(--grey)}

/* legal */
.legal{position:absolute;left:0;top:2640px;width:1200px;height:477px;background:var(--night);color:#d0d0d0;padding:34px 138px 0;font-size:12px;line-height:1.55}
.legal p+p{margin-top:14px}
</style>
</head>
<body>

<header class="site-header">
  <a class="brand" href="#"><span class="brand-dot"></span>pebblemarquis</a>
  <div class="header-right">
    <div class="utility">
      <span class="social-dot"></span><span class="social-dot"></span>
      <span class="search">Search</span>
    </div>
    <nav class="main-nav">
      <a class="current" href="#">Home</a><a href="#">Sign in</a><a href="#">How it works</a><a href="#">Discover a project</a><a href="#">The Baron Blog</a><a href="#">Find out more</a>
    </nav>
  </div>
</header>

<section class="hero">
  <div class="hero-photo" role="img" aria-label="Night city skyline with lit towers over a harbour"></div>
  <div class="hero-content">
    <p class="hero-kicker">THE PEBBLEMARQUIS COMMUNITY IS SOCIAL AND COLLABORATIVE</p>
    <h2 class="hero-title">POOL WITH FRIENDS. SHARE ANY GAINS</h2>
    <a class="btn-ghost" href="#">LEARN MORE</a>
  </div>
  <div class="hero-dots"><span></span><span class="on"></span><span></span></div>
</section>

<section class="intro">
  <h1>PEBBLEMARQUIS IS RECONSTRUCTING A PROPERTY LADDER<br>THAT'S STRONG AND FAIR</h1>
  <p class="lead">By harnessing the power of crowds, it's possible to become a landlord in attractive locations around the world without the burden of financing 100% of the purchase.</p>
  <p class="sub">Leave the day to day management of your property portfolio to us.<br>Start with as little as 1% in a project and plan your steps to becoming a true baron.</p>
</section>

<section class="split">
  <div class="split-panel buy">
    <h2>FIND PROPERTIES</h2>
    <p>Sign up to browse the portfolio. Your journey to becoming a real estate baron starts here.</p>
    <a class="btn-pill btn-light" href="#">BECOME A MEMBER</a>
  </div>
  <div class="split-panel sell">
    <h2>FIND BUYERS</h2>
    <p>Submit a property or development and raise funds from our real estate barons.</p>
    <a class="btn-pill btn-lime" href="#">SUBMIT YOUR PROJECT</a>
  </div>
  <div class="split-badge"><svg width="22" height="22" viewBox="0 0 22 22"><path d="M3 11 L11 4 L19 11 M6 9 V18 H16 V9" fill="none" stroke="#add136" stroke-width="2.5"/></svg></div>
</section>

<section class="projects">
  <h2 class="section-title">FEATURED PROJECTS</h2>
  <p class="section-lead">Brief details of new and popular projects. To view full listings, you will be required tosign up and become a member.</p>
  <div class="cards">
    <article class="card">
      <p class="card-price">From GBP 3,600</p>
      <div class="card-photo" role="img" aria-label="City skyline across the water"></div>
      <h3 class="card-title">14 Ferrow Lane LONDON E1</h3>
      <p class="card-text">Loremos dui tortor, lacinia quis metus eu, varius rutrum nulla. Nunc non turpis nec dolor porta dapibus.</p>
      <div class="progress"><span style="width:0%"></span></div>
      <p class="funded">0% Funded</p>
      <a class="btn-card" href="#">SEE PROJECT DETAILS</a>
    </article>
    <article class="card">
      <p class="card-price">From GBP 3,275</p>
      <div class="card-photo" role="img" aria-label="Harbour towers under a blue sky"></div>
      <h3 class="card-title">Halden Tower, LONDON E14</h3>
      <p class="card-text">Loremos dui tortor, lacinia quis metus eu, varius rutrum nulla. Nunc non turpis nec dolor porta dapibus.</p>
      <div class="progress"><span style="width:4%"></span></div>
      <p class="funded">4% Funded</p>
      <a class="btn-card" href="#">SEE PROJECT DETAILS</a>
    </article>
    <article class="card">
      <p class="card-price">From GBP 760</p>
      <div class="card-photo" role="img" aria-label="Waterfront skyline by day"></div>
      <h3 class="card-title">Riverside Quay E14</h3>
      <p class="card-text">Loremos dui tortor, lacinia quis metus eu, varius rutrum nulla. Nunc non turpis nec dolor porta dapibus.</p>
      <div class="progress"><span style="width:11%"></span></div>
      <p class="funded">11% Funded</p>
      <a class="btn-card" href="#">SEE PROJECT DETAILS</a>
    </article>
  </div>
</section>

<section class="community">
  <h2 class="section-title">BE PART OF A GROWING INTERNATIONAL COMMUNITY</h2>
  <p class="section-lead" style="width:620px">Gain access to new projects in world class cities and join our growing community of international landlords.</p>
  <div class="features">
    <div class="feature">
      <div class="feature-icon"><svg width="28" height="28" viewBox="0 0 28 28"><rect x="5" y="9" width="8" height="15" fill="#fff"/><rect x="15" y="4" width="8" height="20" fill="#fff"/></svg></div>
      <p>Leave the day to day management of your property portfolio to us.</p>
    </div>
    <div class="feature">
      <div class="feature-icon"><svg width="28" height="28" viewBox="0 0 28 28"><circle cx="9" cy="10" r="4" fill="#fff"/><circle cx="19" cy="10" r="4" fill="#fff"/><rect x="3" y="16" width="22" height="7" rx="3" fill="#fff"/></svg></div>
      <p>Collective buying power of the pebblemarquis community</p>
    </div>
    <div class="feature">
      <div class="feature-icon"><svg width="28" height="28" viewBox="0 0 28 28"><circle cx="14" cy="14" r="10" fill="none" stroke="#fff" stroke-width="2.5"/><path d="M4 14 H24 M14 4 C9 10 9 18 14 24 C19 18 19 10 14 4" fill="none" stroke="#fff" stroke-width="2"/></svg></div>
      <p>Attractive real estate from around the world</p>
    </div>
  </div>
</section>

<section class="partners" aria-label="Featured in">
  <svg class="arrow" viewBox="0 0 20 20"><path d="M13 3 L6 10 L13 17" fill="none" stroke="#959595" stroke-width="2"/></svg>
  <span class="partner"></span><span class="partner"></span><span class="partner"></span><span class="partner"></span><span class="partner" style="width:40px"></span><span class="partner"></span>
  <svg class="arrow" viewBox="0 0 20 20"><path d="M7 3 L14 10 L7 17" fill="none" stroke="#959595" stroke-width="2"/></svg>
</section>

<footer class="site-footer">
  <div class="footer-top">
    <nav class="footer-nav">
      <a href="#">Terms of Service</a><a href="#">Privacy Policy</a><a class="current" href="#">How it Works</a><a href="#">Discover a Project</a><a href="#">The Baron Blog</a><a href="#">FAQ</a><a href="#">Find Out More</a>
    </nav>
    <div class="utility"><span class="social-dot"></span><span class="social-dot"></span></div>
  </div>
  <div class="footer-bottom">
    <p class="footer-about">Pebble Marquis is part of the Sproutline Group. The Sproutline Group is a worldwide pioneer and leader in the crowd investing, peer to peer and online investment market.</p>
    <div class="parent-brand"><strong>sproutline<br>group</strong><small>© pebblemarquis 2014</small></div>
  </div>
</footer>

<section class="legal">
  <p>By accessing this site and any pages thereof, you agree to be bound by the terms and conditions. This website is only suitable, intended and available for professional or sophisticated, or similar investors in other jurisdictions, or those who are members of a pebblemarquis community and familiar with, and willing to, accept the risks associated with private participation. Pebblemarquis does not endorse any of the projects that appear on this website, nor does it make any recommendations regarding the appropriateness of particular opportunities for any participant. Each potential participant must review and evaluate the projects at his or her own discretion and determine the suitability of participating.</p>
  <p>This website (the "Site") is in every respect unaffiliated with any site to which it links or any company or entity (and connected projects, investment opportunity or similar) featured on this Site, and is not meant as an endorsement of any of those companies or entities ("third parties"). Furthermore and for the avoidance of doubt, Pebblemarquis Limited is in no way affiliated with any third parties featured or referenced on this Site. There is no commercial relationship between Pebblemarquis Limited and such third parties, nor an agency arrangement or similar. If you believe your Content (including third party content) as each such term is defined in our Terms of Service has been reproduced on the Site without permission, please refer to our Terms of Service for information on how to request its removal from the Site.</p>
</section>

</body>
</html>
```